Business Card Design for DJ

Double-sided full colour business card, with containing the following key information:

DJ Plumwire
Phone (###) ###-####
Email: djplumwire@quillpost.com
Facebook: chatterloom.com/djplumwire
Twitter: @djplumwire

Bringing you the best in Top 40 - Retro - Funk

"It's gonna be a plumwire."

Club/Bar – Weddings – Private Parties - Corporate Events
3000W of portable sound
Dancefloor lighting with optional custom gobos
Available HD Projector and screen
Available custom video production
Free consultation

ERSB Licensed (small logo from http://www.ersbrights.ca)
Member of MNTRK (small logo from http://www.mntrkguild.ca)

• DJ Plumwire logo (attached) or alternative wordmark using type similar to CLUBLAND at http://tunevaultzone.net/uploads/posts/1226228091_6705615x.jpg
• headshot (attached), dance club look/feel

```html
<!DOCTYPE html>
<html lang="en">
<head>
<meta charset="utf-8">
<title>DJ Plumwire – Business Card</title>
<link rel="stylesheet" href="https://fonts.googleapis.com/css2?family=Questrial&display=swap">
<style>
:root{
  --page:#ffffff;
  --card-deep:#0d0612;
  --card-mid:#2a1236;
  --card-high:#4a2160;
  --violet:#b58be0;
  --violet-soft:#8c62b8;
  --ink:#f3ecf8;
  --ink-dim:#cdbfd8;
  --rule:#6b4a80;
  --photo-a:#6a3b7e;
  --photo-b:#2b1436;
}
*{margin:0;padding:0;box-sizing:border-box}
html,body{width:1004px;height:1200px;overflow:hidden;background:var(--page)}
body{font-family:"Questrial",sans-serif;color:var(--ink);position:relative}
.card{position:absolute;left:60px;width:884px;height:505px;overflow:hidden;
  box-shadow:0 10px 24px rgba(0,0,0,.45)}
.card--front{top:49px;
  background:radial-gradient(ellipse 70% 60% at 50% 20%,var(--card-high),var(--card-mid) 45%,var(--card-deep) 100%)}
.card--back{top:618px;
  background:linear-gradient(100deg,var(--card-deep) 0%,var(--card-mid) 55%,var(--card-high) 100%)}

/* front */
.front-mark{position:absolute;left:0;right:0;top:120px;text-align:center;
  font-size:92px;letter-spacing:6px;color:var(--ink)}
.front-tagline{position:absolute;left:0;right:0;top:348px;text-align:center;
  font-size:46px;color:var(--ink);text-shadow:0 0 14px rgba(190,140,240,.8)}
.front-rule{position:absolute;left:127px;width:653px;top:425px;height:1px;
  background:linear-gradient(90deg,transparent,var(--rule) 20%,var(--rule) 80%,transparent)}

/* back */
.back-arcs{position:absolute;inset:0}
.back-name{position:absolute;left:18px;top:12px;font-size:37px;line-height:1;font-weight:400;
  text-shadow:0 0 10px rgba(190,140,240,.6)}
.back-name .accent{color:var(--violet)}
.contact{position:absolute;left:18px;font-size:25px;line-height:1;color:var(--ink-dim)}
.contact--phone{top:57px}
.contact--phone .accent{color:var(--violet)}
.contact--email{top:90px;color:var(--ink)}
.contact--email .accent{color:var(--violet)}
.back-tagline{position:absolute;left:18px;top:140px;font-size:30px;line-height:1}
.back-tagline .accent{color:var(--violet)}
.genres{position:absolute;left:52px;top:181px;font-size:18px;color:var(--violet)}
.genres .bright{color:var(--ink)}
.social{position:absolute;left:538px;display:flex;align-items:center;gap:10px;
  font-size:16px;color:var(--ink-dim)}
.social--one{top:124px}.social--two{top:172px}
.social-dot{width:34px;height:34px;background:var(--violet-soft);border-radius:3px}
.services{position:absolute;left:18px;top:228px;list-style:none;font-size:21px;line-height:27.5px}
.services li::before{content:"";display:inline-block;width:8px;height:8px;border-radius:50%;
  background:var(--ink);margin-right:9px;vertical-align:middle;position:relative;top:-2px}
.back-rule{position:absolute;left:0;width:640px;top:428px;height:1px;background:var(--rule)}
.badge-row{position:absolute;left:18px;top:460px;display:flex;align-items:center;font-size:20px;color:var(--ink)}
.badge{display:inline-block;width:140px;height:24px;background:linear-gradient(90deg,#9fb3e0,#2f3f78);margin-right:12px}
.badge--round{width:64px;height:34px;background:#2c3160;border-radius:4px;margin:0 16px 0 24px}
.back-mark{position:absolute;right:18px;top:40px;font-size:20px;letter-spacing:1px;
  line-height:1;white-space:nowrap;color:var(--ink)}
.photo{position:absolute;left:666px;top:218px;width:218px;height:287px;
  background:linear-gradient(170deg,var(--photo-a),var(--photo-b))}
</style>
</head>
<body>

<section class="card card--front">
  <div class="front-mark">PLUMWIRE</div>
  <p class="front-tagline">It's gonna be a plumwire.</p>
  <div class="front-rule"></div>
</section>

<section class="card card--back">
  <svg class="back-arcs" width="884" height="505" viewBox="0 0 884 505" aria-hidden="true">
    <path d="M520 0 Q700 220 884 260" fill="none" stroke="#6d3f8a" stroke-width="2" opacity=".7"/>
    <path d="M600 0 Q760 170 884 190" fill="none" stroke="#8a55a8" stroke-width="1.5" opacity=".6"/>
    <path d="M450 505 Q560 250 884 120" fill="none" stroke="#5a3272" stroke-width="2" opacity=".6"/>
  </svg>

  <h1 class="back-name">DJ <span class="accent">Plumwire</span></h1>
  <p class="contact contact--phone"><span class="accent">Phone</span> (###) ###-####</p>
  <p class="contact contact--email"><span class="accent">Email:</span> djplumwire@quillpost.com</p>
  <p class="back-tagline">It's gonna be a <span class="accent">plumwire</span>.</p>
  <p class="genres">Bringing you the best in <span class="bright">Top 40 - Retro - Funk</span></p>

  <div class="social social--one"><span class="social-dot"></span>@djplumwire</div>
  <div class="social social--two"><span class="social-dot"></span>chatterloom.com/djplumwire</div>

  <ul class="services">
    <li>Club/Bar – Weddings – Private Parties - Corporate Events</li>
    <li>3000W of portable sound</li>
    <li>Dancefloor lighting with optional custom gobos</li>
    <li>Available HD Projector and screen</li>
    <li>Available custom video production</li>
    <li>Free consultation</li>
  </ul>

  <div class="back-rule"></div>
  <div class="badge-row">
    <span class="badge"></span>ERSB Licensed
    <span class="badge badge--round"></span>Member of MNTRK
  </div>

  <div class="back-mark">PLUMWIRE</div>
  <div class="photo" role="img" aria-label="Headshot of the DJ wearing headphones and sunglasses, with music notes around"></div>
</section>

</body>
</html>
```